Hi,

I am in desperate need of Wordpress website template for for my consulting company. All the graphics are already there, but I need someone who can code that into an extremely nice template for Wordpress (latest version 3.8.1)

I specialize in Consulting and Advise on global software delivery, with a special focus on how to secure innovation within the global delivery platform. I do have the logo and visual identity.

```html
<!DOCTYPE html>
<html lang="en">
<head>
<meta charset="utf-8">
<title>Corvanta – Consulting &amp; Advise on Global Software Delivery</title>
<link href="https://fonts.googleapis.com/css2?family=Questrial&family=Lato:wght@400;700&display=swap" rel="stylesheet">
<style>
:root{
  --navy:#1b4f7a;
  --header-top:#2a6fa0;
  --header-bottom:#1d5c8a;
  --nav-light:#39aef0;
  --nav-dark:#1287d6;
  --teal:#2ab3bd;
  --teal-dark:#1a8f9c;
  --sky:#1aa3e8;
  --orange:#f7a21b;
  --orange-light:#fdc04a;
  --ink:#333;
  --rule:#1f5a86;
  --white:#fff;
  --page:#fff;
}
*{box-sizing:border-box;margin:0;padding:0}
html,body{width:740px;height:1200px;overflow:hidden;background:var(--page)}
body{font-family:'Lato',sans-serif;color:var(--ink);position:relative}
a{text-decoration:none}
.abs{position:absolute}
.site-header{left:0;top:0;width:740px;height:162px;background:linear-gradient(180deg,var(--header-top),var(--header-bottom));border-top:3px solid var(--orange)}
.call-tab{left:508px;top:0;width:142px;height:28px;background:linear-gradient(180deg,var(--orange-light),var(--orange));color:#7a3b00;font:700 11px/28px 'Lato',sans-serif;text-align:center;font-style:italic}
.call-tab b{font-style:normal;color:#5a2a00;font-size:12px;margin-left:4px}
.brand{left:92px;top:62px;display:flex;align-items:center;gap:10px}
.brand-mark{width:30px;height:30px;border-radius:50%;background:var(--nav-light)}
.brand-name{font:700 20px/1 'Lato',sans-serif;color:var(--white)}
.header-title{left:381px;top:56px;font:400 20px/22px 'Questrial',sans-serif;color:var(--white);letter-spacing:.3px}
.main-nav{left:63px;top:129px;width:595px;height:33px;background:linear-gradient(180deg,var(--nav-light),var(--nav-dark));display:flex;clip-path:polygon(2% 0,98% 0,100% 100%,0 100%)}
.main-nav a{flex:1;color:var(--white);font:400 11px/33px 'Questrial',sans-serif;text-align:center;border-right:1px solid rgba(255,255,255,.2)}
.main-nav a:last-child{border:0}
.slider-band{left:0;top:162px;width:740px;height:202px;background:linear-gradient(180deg,var(--teal),var(--teal-dark))}
.slide{left:72px;top:179px;width:578px;height:219px;background:var(--white);box-shadow:0 8px 8px -4px rgba(0,0,0,.45)}
.slide-photo{left:0;top:0;width:326px;height:219px;background:linear-gradient(120deg,#e7e4e2,#c9b4a6 45%,#9b4d44 70%,#d9d6d4)}
.slide-title{left:337px;top:28px;width:236px;font:400 21px/28px 'Questrial',sans-serif;color:var(--sky)}
.btn{display:block;text-align:center;background:linear-gradient(180deg,var(--orange-light),var(--orange));color:#3a2200;font-family:'Questrial',sans-serif;border-bottom:2px solid #d07c00}
.slide-btn{left:337px;top:135px;width:220px;height:32px;font-size:16px;line-height:31px}
.slider-arrow{top:274px}
.dots{left:331px;top:407px;display:flex;gap:3px}
.dots span{width:10px;height:10px;border-radius:50%;background:#d0d0d0;border:1px solid #999}
.dots span.on{background:#777}
.welcome-photo{left:63px;top:442px;width:187px;height:141px;border-radius:50%;border:3px solid #e0e0e0;background:radial-gradient(circle at 55% 45%,#f2d7c4,#c9d4dc 60%,#eef2f5)}
.appt-btn{left:74px;top:592px;width:161px;height:25px;font-size:11px;line-height:24px}
.welcome-kicker{left:274px;top:438px;font:400 15px 'Questrial',sans-serif;color:#222}
.welcome-name{left:274px;top:456px;font:400 21px 'Questrial',sans-serif;color:var(--sky)}
.copy{font-size:8.4px;line-height:12.2px;color:#555}
.welcome-copy{left:274px;top:487px;width:387px}
.welcome-copy p+p{margin-top:10px}
.rule{height:2px;background:var(--rule)}
.more{background:var(--rule);color:var(--white);font:700 7px/13px 'Lato',sans-serif;text-align:center;width:51px;height:14px}
.feature{top:660px;width:156px}
.feature-photo{width:156px;height:72px;border:2px solid #ddd}
.feature h3{font:400 15px 'Questrial',sans-serif;color:var(--sky);text-align:center;margin:12px 0 4px}
.feature .copy{width:156px}
.feature-foot{position:relative;margin-top:9px;height:14px}
.feature-foot .rule{position:absolute;left:0;right:0;top:12px}
.feature-foot .more{position:absolute;right:0;top:0}
.circle-arrow{width:38px;height:38px;top:908px}
.client-photo{left:86px;top:864px;width:128px;height:128px;border-radius:50%;border:4px solid #eee;box-shadow:0 2px 4px rgba(0,0,0,.3);background:radial-gradient(circle at 50% 45%,#f1d2b5,#c9b27a 55%,#8fb55a)}
.client-heading{left:254px;top:858px;font:400 14px 'Questrial',sans-serif;color:var(--sky)}
.client-quote{left:254px;top:889px;width:405px;font-size:11px;line-height:15px;color:#333}
.client-name{left:254px;top:944px;font:700 10.5px 'Lato',sans-serif;color:var(--sky)}
.testi-btn{left:253px;top:970px;width:157px;height:29px;font-size:13px;line-height:28px}
.footer-rule{left:73px;top:1042px;width:592px;height:1px;background:#cfd8df}
.foot-col{top:1063px}
.foot-col h4{font:700 10px 'Lato',sans-serif;color:#222;margin-bottom:8px}
.foot-col li{list-style:none;font-size:8px;line-height:14.5px;color:#555}
.foot-col .hl{color:var(--sky)}
.bottom-rule{left:73px;top:1142px;width:592px;height:1px;background:var(--rule)}
.copyright{left:70px;top:1154px;font-size:8px;color:#444}
.social{top:1150px;width:17px;height:17px}
</style>
</head>
<body>

<header class="site-header abs"></header>
<div class="call-tab abs">CALL US : <b>042-555-0190</b></div>
<div class="brand abs">
  <div class="brand-mark"></div>
  <div class="brand-name">Corvanta</div>
</div>
<h1 class="header-title abs">CONSULTING &amp; ADVISE ON<br>GLOBAL SOFTWARE DELIVERY</h1>
<nav class="main-nav abs">
  <a href="#">HOME</a><a href="#">ABOUT US</a><a href="#">OUR SERVICES</a><a href="#">PACKAGES</a><a href="#">TESTIMONIALS</a><a href="#">CONTACT</a>
</nav>

<section class="slider-band abs"></section>
<div class="slide abs">
  <div class="slide-photo abs" role="img" aria-label="Photo of two young colleagues pointing at a computer screen"></div>
  <h2 class="slide-title abs">how to secure innovation within the global delivery platform</h2>
  <a class="btn slide-btn abs" href="#">READ THE FULL STORY</a>
</div>
<svg class="slider-arrow abs" style="left:32px" width="18" height="30" viewBox="0 0 18 30"><path d="M15 3 4 15l11 12" fill="none" stroke="#fff" stroke-width="5"/></svg>
<svg class="slider-arrow abs" style="left:672px" width="18" height="30" viewBox="0 0 18 30"><path d="M3 3l11 12L3 27" fill="none" stroke="#fff" stroke-width="5"/></svg>
<div class="dots abs"><span></span><span class="on"></span><span></span><span></span><span></span></div>

<div class="welcome-photo abs" role="img" aria-label="Photo of a smiling consultant talking on the phone"></div>
<a class="btn appt-btn abs" href="#">GET AN APPOINTMENT</a>
<div class="welcome-kicker abs">welcome to</div>
<h2 class="welcome-name abs">CORVANTA</h2>
<div class="welcome-copy copy abs">
  <p>Quisque odio nisl, ornare et laoreet ac, molestie porttitor magna. Fusce vel dolor orci. Morbi fermentum, arcu vel dignissim malesuada, turpis enim lacinia augue, quis vestibulum lectus metus congue velit. Nullam venenatis scelerisque arcu in fringilla. Proin lorem mi, ornare eu ultrices vitae, vulputate et velit. Suspendisse potenti. Donec ac aliquet lacus, quis pellentesque nulla. Aliquam sagittis libero odio, nec vehicula nisl aliquet in. In lacinia rhoncus bibendum.</p>
  <p>Nullam commodo vitae eros ac ornare. Suspendisse rhoncus erat tristique libero rutrum, sodales tempor diam gravida. Praesent quis tincidunt urna. Suspendisse potenti. Nullam et metus, lobortis sed</p>
</div>
<div class="rule abs" style="left:274px;top:616px;width:387px"></div>
<div class="more abs" style="left:610px;top:603px">READ MORE</div>

<div class="feature abs" style="left:81px">
  <div class="feature-photo" role="img" aria-label="Photo of a business team meeting" style="background:linear-gradient(120deg,#dfe3e8,#3a4250 50%,#c7ccd3)"></div>
  <h3>Our Mission</h3>
  <p class="copy">Here is our mission statement. Fusce con se quat congue nisl posuere scelerisque. Aen ean sit amet eros ac dui gravida rutr</p>
  <div class="feature-foot"><div class="rule"></div><div class="more">READ MORE</div></div>
</div>
<div class="feature abs" style="left:286px">
  <div class="feature-photo" role="img" aria-label="Photo of a group of business people in suits" style="background:linear-gradient(180deg,#b8bcc2,#2c2f36 60%,#1a1c22)"></div>
  <h3>Our Vision</h3>
  <p class="copy">Here is our mission statement. Fusce con se quat congue nisl posuere scelerisque. Aen ean sit amet eros ac dui gravida rutr</p>
  <div class="feature-foot"><div class="rule"></div><div class="more">READ MORE</div></div>
</div>
<div class="feature abs" style="left:492px">
  <div class="feature-photo" role="img" aria-label="Image of binary digits seen through a magnifying glass" style="background:radial-gradient(circle at 50% 50%,#d6f06a,#3aa88c 55%,#1d5f86)"></div>
  <h3>Our Services</h3>
  <p class="copy">Here is our mission statement. Fusce con se quat congue nisl posuere scelerisque. Aen ean sit amet eros ac dui gravida rutr</p>
  <div class="feature-foot"><div class="rule"></div><div class="more">READ MORE</div></div>
</div>

<svg class="circle-arrow abs" style="left:9px" viewBox="0 0 38 38"><circle cx="19" cy="19" r="17.5" fill="#fff" stroke="#1f5a86" stroke-width="2"/><path d="M22 11l-8 8 8 8" fill="none" stroke="#1f5a86" stroke-width="2.5"/></svg>
<svg class="circle-arrow abs" style="left:683px" viewBox="0 0 38 38"><circle cx="19" cy="19" r="17.5" fill="#fff" stroke="#9fc6dc" stroke-width="1.5"/><path d="M16 11l8 8-8 8" fill="none" stroke="#9fc6dc" stroke-width="2"/></svg>
<div class="client-photo abs" role="img" aria-label="Portrait photo of a client"></div>
<h2 class="client-heading abs">What Client Says About Us</h2>
<p class="client-quote abs">“Curabitur lobortis risus in suscipit accumsan. Vestibulum eget auctor nulla. Pellen tesque vel ligula sollicitudin, bibendum orci sollicitudin, vestibulum sapien. Fusce nulla nibh, semper eu laoreet quis, volutpat vel dolor. ”</p>
<div class="client-name abs">Mark Ellison, CEO Brightform Labs</div>
<a class="btn testi-btn abs" href="#">More Testimonials</a>

<div class="footer-rule abs"></div>
<div class="foot-col abs" style="left:73px"><h4>QUICK LINKS</h4><ul><li>Who We Are</li><li>About Us</li><li>Packages</li></ul></div>
<div class="foot-col abs" style="left:197px"><h4>QUICK LINKS</h4><ul><li>Testimonials</li><li>Terms of Service</li><li>Privacy Policy</li></ul></div>
<div class="foot-col abs" style="left:338px"><h4>LIKE US</h4><ul><li>Like us in Friendbook</li><li>Follow us in Chirper</li><li>Connect Us in Circles+</li></ul></div>
<div class="foot-col abs" style="left:478px"><h4>CONTACT US</h4><ul><li>Suite 12 Level 3, 88 Harbour Lane,</li><li>Sydney NSW 2000</li><li>Tel: <span class="hl">042-555-0190</span></li></ul></div>
<div class="bottom-rule abs"></div>
<div class="copyright abs">© 2014, All Rights Reserved, Corvanta</div>
<div class="social abs" style="left:570px;background:#3b5998"></div>
<div class="social abs" style="left:591px;background:#3fa9e0"></div>
<div class="social abs" style="left:612px;background:#d9432f"></div>

</body>
</html>
```